Brand New Church Business Card Design. Needs to appeal to high school students, professionals.

Business Card. Bold lines and colors. Simple font. This is a new church looking to attract new families who have moved to the area. Business professionals mostly. have a working logo. may need a little tweaking. Church is designed to do excellent ministries for students and children. Like business card design in box on pixel guild homepage. Want a front and back side. Prefer colors to match the logo. But will lean on designers preferences and wisdom. DO NOT WANT A CROSS OR RELIGIOUS SYMBOL on the card.

Target Market(s)

Families, Professionals, Students

Industry/Entity Type

High School

Contact Information for Business Card

SaltRock ChurchSaltRock.atForrest Coulter904-515-8349Forrest@PineHollow.ev

Font styles to use
Sans Serif

Colors
0255a3
ffffff

Requirements
Must have
• Bold colors. Very Masculine. Creative
Nice to have
• On inkmarket.pixelguild.ev homepage in the business card design box. the card with the black, blue and gray looks really sharp. matches our logos.
Should not have
• no crosses or religious symbols.

```html
<!DOCTYPE html>
<html lang="en">
<head>
<meta charset="utf-8">
<title>PineHollow Church – Business Card</title>
<link rel="stylesheet" href="https://fonts.googleapis.com/css2?family=Montserrat:wght@400;500;700&display=swap">
<style>
  :root {
    --stage: #e9eaec;
    --black: #0a0a0a;
    --blue: #0255a3;
    --blue-bright: #1a8fe3;
    --blue-deep: #0b3f9c;
    --paper: #f2f2f2;
    --white: #ffffff;
    --ink-name: #3a4ab0;
    --ink-muted: #555b63;
  }
  * { box-sizing: border-box; margin: 0; padding: 0; }
  html, body { width: 1200px; height: 828px; overflow: hidden; }
  body {
    background: var(--stage);
    font-family: "Montserrat", Arial, sans-serif;
    position: relative;
  }
  .card {
    position: absolute;
    top: 260px;
    width: 540px;
    height: 309px;
    overflow: hidden;
    box-shadow: 0 10px 28px rgba(0,0,0,0.18);
  }
  .card--front { left: 40px; background: var(--black); }
  .card--back { left: 620px; background: var(--paper); }
  .card__art { position: absolute; inset: 0; width: 100%; height: 100%; }

  .brand {
    position: absolute;
    font-weight: 700;
    font-size: 19px;
    line-height: 1;
    white-space: nowrap;
  }
  .card--front .brand { left: 44px; top: 142px; color: var(--white); }
  .card--back .brand { left: 60px; top: 140px; color: var(--blue); }

  .person { position: absolute; left: 60px; top: 222px; }
  .person__name {
    font-weight: 500;
    font-size: 18px;
    letter-spacing: 1px;
    color: var(--ink-name);
    white-space: nowrap;
  }
  .person__role {
    font-size: 11px;
    color: var(--ink-muted);
    margin-top: 3px;
  }

  .contact {
    position: absolute;
    left: 352px;
    top: 96px;
    list-style: none;
    color: var(--white);
    font-size: 9.5px;
  }
  .contact__item {
    display: flex;
    align-items: center;
    gap: 6px;
    height: 19px;
    white-space: nowrap;
  }
  .contact__icon { width: 11px; height: 11px; flex: none; }
</style>
</head>
<body>

<section class="card card--front" aria-label="Card front">
  <svg class="card__art" viewBox="0 0 540 309" preserveAspectRatio="none" role="img" aria-label="Blue and gray wave artwork">
    <defs>
      <linearGradient id="frontBlue" x1="0" y1="0" x2="1" y2="1">
        <stop offset="0" stop-color="var(--blue-bright)"/>
        <stop offset="1" stop-color="var(--blue-deep)"/>
      </linearGradient>
    </defs>
    <path d="M330 0 C310 120 250 250 140 309 L540 309 L540 0 Z" fill="url(#frontBlue)"/>
  </svg>
  <p class="brand">PineHollow Church</p>
</section>

<section class="card card--back" aria-label="Card back">
  <svg class="card__art" viewBox="0 0 540 309" preserveAspectRatio="none" role="img" aria-label="Blue and gray wave artwork">
    <defs>
      <linearGradient id="backBlue" x1="0" y1="0" x2="1" y2="1">
        <stop offset="0" stop-color="var(--blue-bright)"/>
        <stop offset="1" stop-color="var(--blue)"/>
      </linearGradient>
    </defs>
    <path d="M340 0 C332 130 292 250 215 309 L540 309 L540 0 Z" fill="url(#backBlue)"/>
  </svg>

  <p class="brand">PineHollow Church</p>

  <div class="person">
    <p class="person__name">DWAYNE MABRY</p>
    <p class="person__role">Managing Director</p>
  </div>

  <ul class="contact">
    <li class="contact__item">
      <svg class="contact__icon" viewBox="0 0 12 12"><circle cx="6" cy="6" r="6" fill="var(--white)"/><path d="M4 3 L5 3 L5.6 4.6 L4.9 5.2 C5.3 6 6 6.7 6.8 7.1 L7.4 6.4 L9 7 L9 8 C6 8.3 3.7 6 4 3 Z" fill="var(--blue)"/></svg>
      612-473-2096
    </li>
    <li class="contact__item">
      <svg class="contact__icon" viewBox="0 0 12 12"><circle cx="6" cy="6" r="6" fill="var(--white)"/><path d="M4 3 L5 3 L5.6 4.6 L4.9 5.2 C5.3 6 6 6.7 6.8 7.1 L7.4 6.4 L9 7 L9 8 C6 8.3 3.7 6 4 3 Z" fill="var(--blue)"/></svg>
      612-473-2097
    </li>
    <li class="contact__item">
      <svg class="contact__icon" viewBox="0 0 12 12"><circle cx="6" cy="6" r="6" fill="var(--white)"/><rect x="3" y="4" width="6" height="4" fill="none" stroke="var(--blue)" stroke-width="0.9"/><path d="M3 4 L6 6.3 L9 4" fill="none" stroke="var(--blue)" stroke-width="0.9"/></svg>
      Dwayne@PineHollow.ev
    </li>
    <li class="contact__item">
      <svg class="contact__icon" viewBox="0 0 12 12"><circle cx="6" cy="6" r="6" fill="var(--white)"/><circle cx="6" cy="6" r="3" fill="none" stroke="var(--blue)" stroke-width="0.9"/><path d="M3 6 H9" fill="none" stroke="var(--blue)" stroke-width="0.7"/></svg>
      www.PineHollow.ev
    </li>
    <li class="contact__item">
      <svg class="contact__icon" viewBox="0 0 12 12"><circle cx="6" cy="6" r="6" fill="var(--white)"/><path d="M6 9.5 C4.5 7.5 3.8 6.4 3.8 5.2 A2.2 2.2 0 0 1 8.2 5.2 C8.2 6.4 7.5 7.5 6 9.5 Z" fill="var(--blue)"/><circle cx="6" cy="5.2" r="0.8" fill="var(--white)"/></svg>
      18 Fern Mill Road, Dunmore
    </li>
  </ul>
</section>

</body>
</html>
```